Ridgemark Construction Letterhead

Looking for a new professional letter head for our business with one of the two logos on it. It must include all of the information listed below. The company is a heavy construction company and should have something strong looking to go along with the business. Needs to include all of the information we have listed, with nothing added. Looking for something that represents our business well. Would like it to be clean looking with nothing too fancy or colorful. Needs to be bold and strong.

Industry/Entity Type

Construction Company

Font styles to use
Sans Serif

Requirements
Must have
• One of the two logos attached
• Address - 718 Quarry Bend Rd, Ashford Bay, ON K7Q 2K4
• Phone Number - 555-614-3871
• Fax Number - 555-614-3894
• Website - www.ridgemarkconstruction.ca
Nice to have
• Something clean and professional looking
Should not have
• Should not have the words "address", "phone number", etc.
• Only wrote those to have that info included

```html
<!DOCTYPE html>
<html lang="en">
<head>
<meta charset="utf-8">
<title>Ridgemark Construction Letterhead</title>
<link href="https://fonts.googleapis.com/css2?family=Roboto:wght@400;500;700&display=swap" rel="stylesheet">
<style>
:root{
  --backdrop:#333333;
  --paper:#f7f7f5;
  --ink:#1a1a1a;
  --body:#777777;
  --label:#555555;
  --gold:#9a7a2c;
  --sig:#3b5b8a;
}
*{margin:0;padding:0;box-sizing:border-box}
html,body{width:1200px;height:1200px;overflow:hidden;background:var(--backdrop)}
body{font-family:'Roboto',sans-serif}
.sheet{position:absolute;left:279px;top:146px;width:641px;height:906px;background:var(--paper)}
.brand-mark{position:absolute;left:40px;top:57px;width:53px;height:53px;background:var(--gold)}
.brand-name{position:absolute;left:100px;top:58px;font-weight:700;font-size:26px;line-height:26px;color:var(--ink);letter-spacing:.2px;text-transform:uppercase}
.brand-sub{position:absolute;left:100px;top:86px;font-weight:400;font-size:16.5px;line-height:17px;color:var(--ink);letter-spacing:.9px;text-transform:uppercase}
.rule{position:absolute;left:100px;top:83px;width:498px;height:1.5px;background:var(--ink)}
.contact{position:absolute;right:40px;font-size:11.5px;color:var(--ink);text-align:right;line-height:15px;display:flex;align-items:flex-start;gap:6px}
.contact svg{width:10px;height:10px;fill:var(--gold);margin-top:2px;flex:none}
.contact .group{display:flex;align-items:center;gap:6px}
.c-phone{top:48px;gap:10px}
.c-web{top:63px}
.c-addr{top:87px}
.date,.recipient,.greeting,.letter,.signoff{position:absolute;left:40px;font-size:10.6px;color:var(--body)}
.date{top:214px}
.recipient{top:257px;line-height:14.6px;font-style:normal}
.recipient strong{color:var(--label);font-weight:500}
.greeting{top:345px}
.letter{top:374px;width:561px;line-height:14.6px}
.letter p{text-align:justify;margin-bottom:14.6px}
.signoff{top:709px;width:200px}
.signoff .name{font-weight:700;color:var(--label)}
.signature{margin:8px 0 10px;width:146px;height:30px;border-radius:4px;background:linear-gradient(90deg,rgba(59,91,138,.18),rgba(59,91,138,.06))}
</style>
</head>
<body>
<main class="sheet">
  <header>
    <div class="brand-mark"></div>
    <div class="brand-name">Ridgemark</div>
    <div class="rule"></div>
    <div class="brand-sub">Construction</div>
    <div class="contact c-phone">
      <span class="group">555-614-3871
        <svg viewBox="0 0 10 10" aria-label="phone"><path d="M1 4c0-2 8-2 8 0v1H7V4H3v1H1zM2 5h6l1 4H1z"/></svg>
      </span>
      <span class="group">555-614-3894
        <svg viewBox="0 0 10 10" aria-label="fax"><path d="M3 0h4v3H3zM1 3h8v5H7v2H3V8H1zM4 7v2h2V7z"/></svg>
      </span>
    </div>
    <div class="contact c-web">www.ridgemarkconstruction.ca
      <svg viewBox="0 0 10 10" aria-label="website"><circle cx="5" cy="5" r="4.5"/></svg>
    </div>
    <div class="contact c-addr"><span>718 Quarry Bend Rd, Ashford<br>Bay, ON K7Q 2K4</span>
      <svg viewBox="0 0 10 10" aria-label="location"><path d="M5 0a3.5 3.5 0 0 1 3.5 3.5C8.5 6 5 10 5 10S1.5 6 1.5 3.5A3.5 3.5 0 0 1 5 0zm0 2a1.5 1.5 0 1 0 0 3 1.5 1.5 0 0 0 0-3z"/></svg>
    </div>
  </header>

  <p class="date">30/20/2016</p>
  <address class="recipient">
    <strong>Mr. XYZ Smith</strong><br>123, Street No. 123,<br>City Name<br>Pincode-123456
  </address>
  <p class="greeting">Dear Sir,</p>

  <section class="letter">
    <p>Lorem Ipsum is simply dummy text of the printing and typesetting industry. Lorem Ipsum has been the industry's standard dummy text ever since the 1500s, when an unknown printer took a galley of type and scrambled it to make a type specimen book. It has survived not only five centuries, but also the leap into electronic typesetting, remaining essentially unchanged. It was popularised in the 1960s with the release of Lettrex sheets containing Lorem Ipsum passages, and more recently with desktop publishing software like Folio Layout including versions of Lorem Ipsum.</p>
    <p>Lorem Ipsum is simply dummy text of the printing and typesetting industry. Lorem Ipsum has been the industry's standard dummy text ever since the 1500s, when an unknown printer took a galley of type and scrambled it to make a type specimen book. It has survived not only five centuries, but also the leap into electronic typesetting, remaining essentially unchanged. It was popularised in the 1960s with the release of Lettrex sheets containing Lorem Ipsum passages, and more recently with desktop publishing software like Folio Layout including versions of Lorem Ipsum.</p>
    <p>Lorem Ipsum is simply dummy text of the printing and typesetting industry. Lorem Ipsum has been the industry's standard dummy text ever since the 1500s, when an unknown printer took a galley of type and scrambled it to make a type specimen book.</p>
    <p>Lorem Ipsum is simply dummy text of the printing and typesetting industry. Lorem Ipsum has been the industry's standard dummy text ever since the 1500s, when an unknown printer took a galley of type and scrambled it to make a type specimen book.</p>
  </section>

  <footer class="signoff">
    <p class="name">Your Name</p>
    <div class="signature" role="img" aria-label="Handwritten signature"></div>
    <p>CEO&nbsp; | &nbsp;Owner</p>
  </footer>
</main>
</body>
</html>
```